Verdana Glen Website

I need a design of homepage for a health and wellness center. We considers self to be young and fresh and want something along that design. We want a main picture/logo/design (or all three), and underneath that 4 pictures to depict what services we do. The four services are Orthopedic Rehab, Neurological Rehab, Speech Pathology and Float. I have attached our logo, and some pictures that might be helpful, but the pictures don't have to be included. Here is an example of what I would like it look. http://pixelquarry.com/web-design/contests/brimlotts-website-design-needed-more-work-come-submit-517306/entries/84162975

Health

```html
<!DOCTYPE html>
<html lang="en">
<head>
<meta charset="utf-8">
<title>Verdana Glen Health &amp; Wellness</title>
<link href="https://fonts.googleapis.com/css2?family=Open+Sans:wght@400;600;700;800&display=swap" rel="stylesheet">
<style>
:root{
  --lime:#8cc63f;
  --lime-dark:#6fa52a;
  --teal:#2f6f66;
  --mint:#e4f2ec;
  --mint-deep:#cfe7dd;
  --ink:#3d3d3d;
  --muted:#777;
  --rule:#e2e2e2;
  --panel:#f1f1f1;
  --footer:#e9e9e9;
}
*{box-sizing:border-box;margin:0;padding:0}
html,body{width:742px;height:1200px;overflow:hidden}
body{font-family:"Open Sans",Arial,sans-serif;color:var(--ink);background:#fff;font-size:7px;line-height:1.45}
.page{width:742px;height:1200px;position:relative;overflow:hidden}
.wrap{width:650px;margin:0 auto;position:relative}

/* top bar */
.topbar{height:24px;border-bottom:1px solid var(--rule)}
.topbar .wrap{display:flex;justify-content:space-between;align-items:center;height:24px}
.util-links{display:flex;gap:5px;font-size:6px;color:var(--muted);text-transform:uppercase}
.account{display:flex;gap:4px}
.btn-small{background:var(--lime);color:#fff;font-size:6px;font-weight:700;padding:3px 8px;text-transform:uppercase}

/* header */
.header .wrap{display:flex;justify-content:space-between;align-items:center;height:52px}
.brand{display:flex;align-items:center;gap:6px}
.brand-mark{width:18px;height:18px;background:var(--lime)}
.brand-name{font-size:16px;font-weight:700;color:var(--teal);letter-spacing:.5px}
.nav{display:flex;gap:14px;font-size:7.5px;font-weight:700;text-transform:uppercase;color:var(--ink)}

/* hero */
.hero{height:240px;background:linear-gradient(180deg,#f2f9f6 0%,var(--mint) 100%);position:relative}
.hero .wrap{height:240px}
.hero-copy{position:absolute;left:20px;top:68px;width:230px}
.hero-title{font-size:19px;font-weight:700;color:var(--lime-dark);line-height:1.2;text-transform:uppercase}
.hero-text{margin:8px 0 10px;color:var(--muted);font-size:7px}
.btn{display:inline-block;background:var(--lime);color:#fff;font-weight:700;font-size:6.5px;padding:5px 10px;text-transform:uppercase}
.hero-art{position:absolute;left:380px;top:28px;width:180px;height:180px;border-radius:50%;background:radial-gradient(circle,#ffffff 0%,var(--mint-deep) 100%)}
.dots{position:absolute;left:50%;bottom:10px;display:flex;gap:4px;transform:translateX(-50%)}
.dots span{width:5px;height:5px;border-radius:50%;background:#b9d7c9}
.dots span.on{background:var(--teal)}

/* welcome */
.welcome .wrap{display:flex;gap:30px;padding-top:54px;height:176px}
.welcome-tag{position:relative;width:122px;height:62px;flex:none}
.welcome-tag svg{position:absolute;left:0;top:0}
.welcome-tag p{position:relative;color:#fff;font-weight:800;font-size:8px;line-height:1.25;padding:9px 0 0 12px;text-transform:uppercase}
.welcome-text{flex:1;color:var(--muted);padding-top:2px}
.welcome-text p+p{margin-top:6px}

/* services */
.services{text-align:center}
.section-title{font-size:11px;font-weight:700;color:var(--ink);text-transform:uppercase;letter-spacing:.3px}
.title-rule{width:26px;height:2px;background:var(--lime);margin:5px auto 0}
.service-grid{display:flex;justify-content:space-between;margin-top:16px}
.service{width:145px}
.service-art{width:74px;height:74px;margin:0 auto;border-radius:50%;background:linear-gradient(160deg,#f4faef,#dcedc8);border:2px solid #eef5e6}
.service h3{font-size:7.5px;font-weight:700;text-transform:uppercase;margin:10px 0 5px}
.service p{font-size:6.3px;color:var(--muted);height:44px}
.btn-block{display:block;background:var(--lime);color:#fff;font-weight:700;font-size:6.5px;padding:5px 0;text-transform:uppercase}

/* news + ask */
.lower{background:var(--panel);margin-top:44px;height:228px}
.lower .wrap{display:flex;gap:28px;padding-top:14px}
.col{flex:1}
.col-head{display:flex;align-items:center;gap:6px;border-bottom:1px solid #d6d6d6;padding-bottom:6px}
.col-head .square{width:16px;height:16px;background:var(--lime);display:flex;align-items:center;justify-content:center}
.col-head h2{font-size:11px;font-weight:700;text-transform:uppercase}
.news h4{font-size:7px;font-weight:700;margin:12px 0 6px}
.news p{font-size:6.3px;color:var(--muted)}
.news .btn{margin-top:12px}
.form{padding-top:10px}
.field-row{display:flex;gap:10px}
.field{flex:1;margin-top:6px}
.field label{display:block;font-size:6px;margin-bottom:2px}
.box{height:14px;background:#fff;border:1px solid #d8d8d8}
.box.select{width:120px;font-size:6px;color:var(--muted);padding:2px 4px}
.box.area{height:34px}
.form .btn{margin-top:7px;padding:4px 12px}

/* testimonial */
.testimonial .wrap{padding-top:50px}
.testimonial h2{font-size:11px;font-weight:700;text-transform:uppercase;border-bottom:1px solid var(--rule);padding-bottom:5px}
.testimonial blockquote{font-size:6.5px;color:var(--muted);margin-top:8px}
.testimonial cite{display:block;text-align:right;font-style:normal;font-size:6.3px;color:var(--ink);margin-top:5px}

/* footer */
.footer{position:absolute;left:0;bottom:0;width:742px;height:30px;background:var(--footer)}
.footer .wrap{display:flex;justify-content:space-between;align-items:center;height:30px}
.footer p{font-size:6px;color:var(--muted)}
.social{display:flex;gap:4px}
.social span{width:11px;height:11px;border-radius:50%;background:var(--teal)}
</style>
</head>
<body>
<div class="page">

  <div class="topbar">
    <div class="wrap">
      <div class="util-links"><span>Contact</span><span>|</span><span>Ask a Question</span><span>|</span><span>Physician Login</span><span>|</span><span>Press</span></div>
      <div class="account"><span class="btn-small">Sign In</span><span class="btn-small">Register</span></div>
    </div>
  </div>

  <header class="header">
    <div class="wrap">
      <div class="brand"><span class="brand-mark"></span><span class="brand-name">VERDANA GLEN</span></div>
      <nav class="nav"><span>Home</span><span>About Us</span><span>Health</span><span>Wellness Services</span><span>Mind-Body Initiative</span></nav>
    </div>
  </header>

  <section class="hero">
    <div class="wrap">
      <div class="hero-copy">
        <h1 class="hero-title">Where Expertise<br>Quality Care Meet</h1>
        <p class="hero-text">Lorem ipsum dolor sit amet, consectetur adipiscing elit, sed do eiusmod tempor.</p>
        <span class="btn">Read More</span>
      </div>
      <div class="hero-art" role="img" aria-label="Circular green leaf emblem illustration"></div>
    </div>
    <div class="dots"><span class="on"></span><span></span><span></span></div>
  </section>

  <section class="welcome">
    <div class="wrap">
      <div class="welcome-tag">
        <svg width="122" height="62" viewBox="0 0 122 62"><polygon points="0,0 106,0 122,31 106,62 0,62" fill="#8cc63f"/></svg>
        <p>Welcome to<br>Verdana Glen<br>Health Wellness<br>Center</p>
      </div>
      <div class="welcome-text">
        <p>We are proud to be New York City's first comprehensive health &amp; wellness center. Our professional philosophy is to provide personal rehabilitation, medical and wellness services in a supportive and nurturing environment.</p>
        <p>We strive to foster optimal health and well-being in order to improve the quality of life for each of our patients.</p>
      </div>
    </div>
  </section>

  <section class="services">
    <div class="wrap">
      <h2 class="section-title">Our Services</h2>
      <div class="title-rule"></div>
      <div class="service-grid">
        <div class="service">
          <div class="service-art" role="img" aria-label="Orthopedic rehab illustration"></div>
          <h3>Orthopedic Rehab</h3>
          <p>Lorem ipsum dolor sit amet, consectetur adipiscing elit, sed do eiusmod tempor incididunt ut labore et dolore magna aliqua.</p>
          <span class="btn-block">Learn More</span>
        </div>
        <div class="service">
          <div class="service-art" role="img" aria-label="Neurological rehab illustration"></div>
          <h3>Neurological Rehab</h3>
          <p>Lorem ipsum dolor sit amet, consectetur adipiscing elit, sed do eiusmod tempor incididunt ut labore et dolore magna aliqua.</p>
          <span class="btn-block">Learn More</span>
        </div>
        <div class="service">
          <div class="service-art" role="img" aria-label="Speech pathology illustration"></div>
          <h3>Speech Pathology</h3>
          <p>Lorem ipsum dolor sit amet, consectetur adipiscing elit, sed do eiusmod tempor incididunt ut labore et dolore magna aliqua.</p>
          <span class="btn-block">Learn More</span>
        </div>
        <div class="service">
          <div class="service-art" role="img" aria-label="Floatation meditation illustration"></div>
          <h3>Floatation Meditation</h3>
          <p>Lorem ipsum dolor sit amet, consectetur adipiscing elit, sed do eiusmod tempor incididunt ut labore et dolore magna aliqua.</p>
          <span class="btn-block">Learn More</span>
        </div>
      </div>
    </div>
  </section>

  <section class="lower">
    <div class="wrap">
      <div class="col news">
        <div class="col-head">
          <span class="square"><svg width="9" height="9" viewBox="0 0 9 9"><rect x="1" y="1" width="7" height="7" fill="none" stroke="#fff" stroke-width="1"/><line x1="2.5" y1="3.5" x2="6.5" y2="3.5" stroke="#fff"/><line x1="2.5" y1="5.5" x2="6.5" y2="5.5" stroke="#fff"/></svg></span>
          <h2>In the News</h2>
        </div>
        <h4>Celebrate Better Speech &amp; Hearing Month by Considering Telehealth as an Addition to Your Practice</h4>
        <p>Thanks to Lena Morrow for sharing the new ways technology can support therapy. Lena is the founder of Brightwater Speech Studio, a licensed speech-language pathologist and a lecturer on motor speech and swallowing care. Her studio offers sessions in Midtown and on the Upper West Side of Manhattan.</p>
        <span class="btn">Read More</span>
      </div>
      <div class="col">
        <div class="col-head">
          <span class="square"><svg width="9" height="9" viewBox="0 0 9 9"><path d="M1 1h7v5H4L2 8V6H1z" fill="#fff"/></svg></span>
          <h2>Ask a Question</h2>
        </div>
        <div class="form">
          <div class="field-row">
            <div class="field"><label>Your Name*</label><div class="box"></div></div>
            <div class="field"><label>Your Email*</label><div class="box"></div></div>
          </div>
          <div class="field"><label>Services *</label><div class="box select">Physical Therapy</div></div>
          <div class="field"><label>Your Question / Query*</label><div class="box area"></div></div>
          <span class="btn">Submit</span>
        </div>
      </div>
    </div>
  </section>

  <section class="testimonial">
    <div class="wrap">
      <h2>Testimonial</h2>
      <blockquote>Tessa Quill works from a convenient location, yet that wasn't my first impression. It began when I first spoke with Tessa. I had spoken with several speech therapists about my issue before her, and I knew after our talk that my search was complete.</blockquote>
      <cite>- Rhea, Midtown, NY</cite>
    </div>
  </section>

  <footer class="footer">
    <div class="wrap">
      <p>Copyright 2014 Verdana Glen Physical Therapy &amp; Pilates. All rights reserved. &nbsp; Term And Condition | Privacy Policy</p>
      <div class="social"><span></span><span></span><span></span></div>
    </div>
  </footer>

</div>
</body>
</html>
```